How likely are people to engage in social distancing? We need a good illustration to show the data!

We surveyed U.S. adults March 20th - 24th, 2020 and asked how likely they were to engage in social distancing (and other COVID-19 related health behaviors). What did the survey find? Basically, most people intend to engage in social distancing behaviors (e.g., avoiding large crowds) and other behaviors that reduce the spread of COVID-19 (e.g., washing hands at least 20 seconds). When most people intend to engage in a behavior, then public health professionals try to leverage that to move more people to act.
Now we need innovative and professional images that attempt to communicate one or all of these findings. The specific findings are nicely summarized in the attached document. For example, 82% of participants intend to engage in social distancing.
What sort of visual are we looking for? Our preference is for an original illustration (or set of illustrations). Our preference is for (creative and powerful illustrations, but we are also open to the creative and well-executed infographics.
We need these images fast . We will award monetary prizes to the 3 best designs. If we like more than that, then we might purchase more (e.g., in past contests, we have purchased as many as 30 designs).
What we will need:
(1) The illustrations must be original and we will need the photoshop and/or illustrator files for all artwork.
(2) You can illustrate all of the findings or just one of them. We need creative approaches that do a lucid job of bringing the data to life. Most people intend to engage in these behaviors. How to communicate that? Corvantists and Halmerites do not differ in their intentions; how to communicate that?
(3) The illustration should say, somewhere: "Based on a survey of 400 U.S. adults conducted March 20 - 24th, 2020."

U.S. Adults

• Original illustrations based on the findings of the survey (see attached document).

```html
<!DOCTYPE html>
<html lang="en">
<head>
<meta charset="utf-8">
<title>Novel Coronavirus – Hand Washing</title>
<link rel="stylesheet" href="https://fonts.googleapis.com/css2?family=Playfair+Display:wght@700&family=Patrick+Hand&display=swap">
<style>
  :root {
    --page: #efefef;
    --pale-yellow: #eef7a2;
    --sky: #7ad5f4;
    --lime: #bdf08c;
    --meadow: #d3f78b;
    --pool: #5fe0fb;
    --pool-edge: #68b0e4;
    --title-blue: #6497cf;
    --virus-green: #72c466;
    --virus-edge: #5ba0e0;
    --note-teal: #6fbfd0;
    --note-green: #8fd08a;
    --note-yellow: #f4f8a6;
    --survey-text: #b9d86e;
    --skin: #efd8b6;
    --lather: #e6cdea;
  }
  * { box-sizing: border-box; margin: 0; padding: 0; }
  html, body { width: 1200px; height: 1000px; overflow: hidden; background: var(--page); }
  .canvas { position: relative; width: 1200px; height: 1000px; overflow: hidden; }
  .backdrop { position: absolute; left: 0; top: 0; }
  .title {
    position: absolute; left: 55px; top: 186px;
    font-family: "Playfair Display", serif; font-weight: 700;
    font-size: 70px; line-height: 1; letter-spacing: 1px;
    color: var(--title-blue);
  }
  .virus { position: absolute; }
  .virus--large { left: 830px; top: 75px; }
  .virus--small { left: 830px; top: 290px; }
  .lettering { position: absolute; left: 30px; top: 515px; width: 200px; height: 105px; border-radius: 30px; background: #56cdef; }
  .hands {
    position: absolute; left: 95px; top: 640px; width: 330px; height: 220px; border-radius: 90px 70px 60px 80px;
    background: linear-gradient(120deg, var(--skin) 40%, var(--lather));
  }
  .findings {
    position: absolute; left: 595px; top: 440px; width: 570px;
    font-family: "Patrick Hand", sans-serif; font-size: 42px; line-height: 1;
    color: var(--note-teal);
  }
  .findings li { list-style: none; height: 70px; white-space: nowrap; }
  .findings .stat { color: var(--note-green); }
  .survey-note {
    position: absolute; left: 595px; top: 772px; width: 570px;
    font-family: "Patrick Hand", sans-serif; font-size: 31px; line-height: 40px;
    color: var(--survey-text);
  }
</style>
</head>
<body>
<main class="canvas">
  <svg class="backdrop" width="1200" height="1000" viewBox="0 0 1200 1000" aria-hidden="true">
    <rect x="0" y="75" width="1200" height="22" fill="var(--pale-yellow)"/>
    <rect x="0" y="97" width="1200" height="55" fill="var(--sky)"/>
    <rect x="0" y="150" width="1200" height="152" fill="var(--lime)"/>
    <rect x="0" y="300" width="1200" height="100" fill="var(--sky)"/>
    <path d="M0 388 Q600 350 1200 388 L1200 925 L0 925 Z" fill="var(--meadow)"/>
    <rect x="560" y="735" width="640" height="24" fill="var(--note-yellow)"/>
    <rect x="590" y="858" width="580" height="14" fill="var(--note-yellow)"/>
    <path d="M0 452 C120 445 230 470 300 515 L420 610 C500 690 555 800 570 925 L0 925 Z"
          fill="var(--pool)" stroke="var(--pool-edge)" stroke-width="10"/>
    <circle cx="410" cy="512" r="113" fill="var(--pool)" stroke="var(--pool-edge)" stroke-width="12"/>
    <g class="stopwatch">
      <rect x="392" y="452" width="36" height="16" rx="6" fill="#8fe6f6" stroke="#5ba6d6" stroke-width="5"/>
      <circle cx="410" cy="522" r="58" fill="#7fe3f5" stroke="#5ba6d6" stroke-width="8"/>
      <path d="M410 522 L410 470 A52 52 0 0 1 452 500 Z" fill="#5ba6d6" opacity="0.6"/>
    </g>
  </svg>

  <h1 class="title">NOVEL CORONAVIRUS</h1>

  <svg class="virus virus--large" width="370" height="350" viewBox="0 0 370 350" role="img" aria-label="Large green coronavirus particle illustration">
    <circle cx="290" cy="130" r="190" fill="var(--virus-green)" stroke="var(--virus-edge)" stroke-width="14"/>
  </svg>
  <svg class="virus virus--small" width="150" height="120" viewBox="0 0 150 120" role="img" aria-label="Small green coronavirus particle illustration">
    <circle cx="70" cy="56" r="45" fill="var(--virus-green)"/>
  </svg>

  <div class="lettering" role="img" aria-label="Hand-lettered note: min 20 sec"></div>
  <div class="hands" role="img" aria-label="Illustration of soapy hands being washed"></div>

  <ul class="findings">
    <li><span class="stat">82%</span> intend social distancing</li>
    <li>avoid large crowds, stay home</li>
    <li>wash hands at least 20 sec</li>
    <li>• Corvantists = Halmerites</li>
  </ul>
  <p class="survey-note">Based on a survey of 400 U.S. adults<br>conducted March 20 - 24th, 2020.</p>
</main>
</body>
</html>
```